Steadfast MD - Sleep Medicine Specialist - Business Cards

We are a new medical practice called Steadfast MD. We are sleep medicine specialists and we will be conducting sleep studies on patients with sleep related ailments. We want the business card to be bold, professional, and clean with the logo as the stand out visual piece. We dont like wild flashy designs. We want our design to be bold and classic while at the same time conveying who we are and what we do. We are reliable, professional, and the best in the business.

Industry/Entity Type

Health Care

Contact Information for Business Card

- Clean
- Bold
- Classic
- not cluttered

Requirements
Must have
• logo, website, phone number
Nice to have
• several options to choose from
Should not have
• flashy imaged - reflective print - images of people sleeping

```html
<!DOCTYPE html>
<html lang="en">
<head>
<meta charset="utf-8">
<title>Steadfast MD – Business Cards</title>
<link href="https://fonts.googleapis.com/css2?family=Montserrat:wght@400;500;800&display=swap" rel="stylesheet">
<style>
  :root {
    --paper: #f3f3f3;
    --card-white: #ffffff;
    --brand-red: #cc1f26;
    --ink: #1c1c1c;
    --rule: #8a8a8a;
    --muted: #3a3a3a;
  }
  html, body {
    margin: 0;
    width: 1200px;
    height: 963px;
    overflow: hidden;
    background: var(--paper);
    font-family: "Montserrat", sans-serif;
  }
  .sheet {
    position: relative;
    width: 1200px;
    height: 963px;
    display: flex;
    align-items: center;
    justify-content: center;
    gap: 40px;
  }
  .card {
    position: relative;
    width: 525px;
    height: 300px;
    box-sizing: border-box;
    box-shadow: 0 6px 18px rgba(0,0,0,0.10);
    overflow: hidden;
  }

  /* Front: contact side */
  .card-front { background: var(--card-white); color: var(--ink); }
  .person {
    position: absolute;
    left: 36px;
    top: 34px;
  }
  .person-name {
    margin: 0;
    font-weight: 800;
    font-size: 22px;
    letter-spacing: 0.2px;
  }
  .person-title {
    margin: 2px 0 0;
    font-size: 11px;
    font-weight: 400;
    color: var(--muted);
  }
  .divider {
    position: absolute;
    left: 36px;
    right: 36px;
    top: 92px;
    height: 1px;
    background: var(--rule);
  }
  .contact-list {
    position: absolute;
    left: 36px;
    top: 108px;
    margin: 0;
    padding: 0;
    list-style: none;
    font-size: 12px;
    line-height: 20px;
    color: var(--muted);
  }
  .contact-list li { display: flex; align-items: center; gap: 8px; }
  .contact-icon { width: 11px; height: 11px; flex: none; }
  .wordmark {
    display: flex;
    align-items: center;
    gap: 12px;
  }
  .wordmark-mark {
    width: 46px;
    height: 46px;
    border-radius: 50%;
    box-sizing: border-box;
    flex: none;
  }
  .wordmark-name {
    font-weight: 800;
    font-size: 30px;
    letter-spacing: -0.5px;
    white-space: nowrap;
  }
  .card-front .wordmark {
    position: absolute;
    right: 34px;
    top: 128px;
  }
  .card-front .wordmark-mark { border: 3px solid var(--brand-red); }
  .card-front .wordmark-name { color: var(--ink); }
  .address-rule {
    position: absolute;
    right: 36px;
    bottom: 86px;
    width: 200px;
    height: 1px;
    background: var(--rule);
  }
  .address {
    position: absolute;
    right: 36px;
    bottom: 22px;
    margin: 0;
    font-style: normal;
    font-size: 12px;
    line-height: 19px;
    color: var(--muted);
    text-align: left;
    width: 200px;
  }

  /* Back: brand side */
  .card-back {
    background: var(--brand-red);
    color: #fff;
  }
  .card-back .wordmark {
    position: absolute;
    left: 70px;
    top: 96px;
  }
  .card-back .wordmark-mark { border: 3px solid #fff; }
  .card-back .wordmark-name { color: #fff; }
  .back-url {
    position: absolute;
    left: 128px;
    top: 168px;
    margin: 0;
    font-weight: 500;
    font-size: 13px;
    letter-spacing: 1.5px;
  }
</style>
</head>
<body>
<main class="sheet">
  <section class="card card-front" aria-label="Business card front">
    <div class="person">
      <h1 class="person-name">Daniel Hayes</h1>
      <p class="person-title">Managing Partner</p>
    </div>
    <div class="divider"></div>
    <ul class="contact-list">
      <li>
        <svg class="contact-icon" viewBox="0 0 12 12" aria-hidden="true"><path d="M3 1 L5 3.5 L4 5 Q5 7 7 8 L8.5 7 L11 9 L9.5 11 Q4 10.5 1 2.5 Z" fill="none" stroke="#cc1f26" stroke-width="1"/></svg>
        000 000 0000
      </li>
      <li>
        <svg class="contact-icon" viewBox="0 0 12 12" aria-hidden="true"><rect x="0.5" y="2.5" width="11" height="7" fill="none" stroke="#cc1f26" stroke-width="1"/><path d="M0.5 2.5 L6 7 L11.5 2.5" fill="none" stroke="#cc1f26" stroke-width="1"/></svg>
        daniel@steadfastmd.com
      </li>
      <li>
        <svg class="contact-icon" viewBox="0 0 12 12" aria-hidden="true"><circle cx="6" cy="6" r="5.3" fill="none" stroke="#cc1f26" stroke-width="1"/><ellipse cx="6" cy="6" rx="2.3" ry="5.3" fill="none" stroke="#cc1f26" stroke-width="1"/><path d="M0.7 6 H11.3 M1.5 3.5 H10.5 M1.5 8.5 H10.5" stroke="#cc1f26" stroke-width="0.8"/></svg>
        www.steadfastmd.com
      </li>
    </ul>
    <div class="wordmark">
      <span class="wordmark-mark" aria-hidden="true"></span>
      <span class="wordmark-name">Steadfast MD</span>
    </div>
    <div class="address-rule"></div>
    <address class="address">
      418 N Willow Avenue<br>
      Linden, MS 39150<br>
      Ca Blabla Bla Bla
    </address>
  </section>

  <section class="card card-back" aria-label="Business card back">
    <div class="wordmark">
      <span class="wordmark-mark" aria-hidden="true"></span>
      <span class="wordmark-name">Steadfast MD</span>
    </div>
    <p class="back-url">www.steadfastmd.com</p>
  </section>
</main>
</body>
</html>
```